Business Card Design Project

I require a business card with the following information on them for various different people;
name
m:
f:
e:
I have a logo already and will attached that. We are in the construction industry. I require something clean and simple but eye catching at the same time. You can use another colour with our logo if you like and you can style the logo as well if you wish. I am open.
Also it needs to be front and back design.
Industry/Entity Type
Construction
Requirements
Must have
- Logo, name, mobile, fax and email address.
Front and back design

```html
<!DOCTYPE html>
<html lang="en">
<head>
<meta charset="utf-8">
<title>Greywood Developments – Business Card</title>
<link rel="stylesheet" href="https://fonts.googleapis.com/css2?family=Open+Sans:wght@400;600;700&display=swap">
<style>
  :root {
    --backdrop: #e8e5e0;
    --card: #ffffff;
    --brand-green: #4aa83c;
    --pill-light: #a9cf5a;
    --pill-dark: #3a7a28;
    --ink: #4a4a4a;
    --card-shadow: rgba(0, 0, 0, 0.35);
  }
  * { margin: 0; padding: 0; box-sizing: border-box; }
  html, body {
    width: 1200px;
    height: 407px;
    overflow: hidden;
    background: var(--backdrop);
    font-family: "Open Sans", Arial, sans-serif;
  }
  .canvas {
    position: relative;
    width: 1200px;
    height: 407px;
  }
  .card {
    position: absolute;
    top: 60px;
    width: 502px;
    height: 288px;
    background: var(--card);
    box-shadow: 4px 5px 6px var(--card-shadow);
  }
  .card--front { left: 58px; }
  .card--back { left: 639px; }

  .brand {
    position: absolute;
    left: 0;
    right: 0;
    display: flex;
    align-items: center;
    justify-content: center;
    gap: 12px;
  }
  .card--front .brand { top: 58px; }
  .card--back .brand { top: 124px; }
  .brand__square {
    width: 30px;
    height: 30px;
    background: var(--brand-green);
  }
  .brand__name {
    font-family: "Open Sans", Arial, sans-serif;
    font-weight: 400;
    font-size: 32px;
    letter-spacing: 0.5px;
    color: var(--brand-green);
    line-height: 1;
  }

  .name-pill {
    position: absolute;
    left: 149px;
    top: 158px;
    width: 203px;
    height: 34px;
    border-radius: 9px;
    background: linear-gradient(90deg, var(--pill-light) 0%, #6aaa3e 45%, var(--pill-dark) 100%);
    box-shadow: 0 8px 8px -4px rgba(0, 0, 0, 0.35);
    display: flex;
    align-items: center;
    justify-content: center;
    color: #ffffff;
    white-space: nowrap;
  }
  .name-pill__name { font-weight: 700; font-size: 16px; }
  .name-pill__title { font-weight: 400; font-size: 13px; margin-left: 5px; }

  .contact {
    position: absolute;
    left: 0;
    right: 0;
    top: 251px;
    text-align: center;
    font-size: 12.5px;
    color: var(--ink);
    word-spacing: 1px;
  }
  .contact span + span { margin-left: 10px; }
</style>
</head>
<body>
  <main class="canvas">
    <section class="card card--front" aria-label="Card front">
      <div class="brand">
        <div class="brand__square"></div>
        <div class="brand__name">Greywood Developments</div>
      </div>
      <div class="name-pill">
        <span class="name-pill__name">Your Name</span>
        <span class="name-pill__title">/ Title</span>
      </div>
      <p class="contact">
        <span>c : 123-456-7890</span>
        <span>f : 123-456-7890</span>
        <span>e : name@website.com</span>
      </p>
    </section>

    <section class="card card--back" aria-label="Card back">
      <div class="brand">
        <div class="brand__square"></div>
        <div class="brand__name">Greywood Developments</div>
      </div>
    </section>
  </main>
</body>
</html>
```